Cover für Gedichtbuch
Zielgruppe
Das Buch soll jungen und alten Menschen gefallen. Zielgruppe sind aber vor allem junge Leser zwischen 18 und Mitte 20.
Aufgabenstellung
Für das Erstlingswerk von zwei Nachwuchsautoren wird ein Wendecover gesucht. Sprich: Auf der einen Seite stehen Gedichte mit hellen Gedichten (Liebe, Freude, Glück) - die andere Hälfte besteht aus dunklen Gedichten (Tod, Depression). Das Buch soll gedreht werden. Daher sollen die beiden Coverseiten einen Kontrast darstellen.

```html
<!DOCTYPE html>
<html lang="de">
<head>
<meta charset="utf-8">
<title>Gedichte – dunkle und helle Seite</title>
<link rel="stylesheet" href="https://fonts.googleapis.com/css2?family=Cormorant+Garamond:wght@500;600&display=swap">
<style>
  :root {
    --night: #000000;
    --amber: #b8631f;
    --amber-deep: #6a3410;
    --umber: #4a2710;
    --paper: #ffffff;
    --ink-shadow: rgba(0,0,0,0.85);
  }
  html, body {
    margin: 0;
    padding: 0;
    width: 1200px;
    height: 845px;
    overflow: hidden;
    background: var(--paper);
  }
  .cover {
    position: relative;
    width: 1200px;
    height: 845px;
    overflow: hidden;
    background: var(--paper);
    font-family: "Cormorant Garamond", "Times New Roman", serif;
  }
  .side {
    position: absolute;
    top: 0;
    height: 845px;
  }
  .side--dark {
    left: 0;
    width: 592px;
    background: linear-gradient(to bottom,
      var(--night) 0%, var(--night) 14%,
      var(--amber-deep) 22%, var(--amber) 32%,
      var(--amber) 62%, var(--amber-deep) 78%,
      var(--night) 90%, var(--night) 100%);
  }
  .side--light {
    left: 602px;
    width: 598px;
    background: linear-gradient(to bottom,
      var(--paper) 0%, var(--paper) 12%,
      #d9b08a 20%, var(--umber) 34%,
      var(--amber-deep) 52%, var(--umber) 66%,
      #c99366 74%, var(--paper) 86%, var(--paper) 100%);
  }
  .title {
    position: absolute;
    margin: 0;
    color: var(--paper);
    font-weight: 500;
    line-height: 1;
    white-space: nowrap;
    letter-spacing: 2px;
  }
  .title--dunkle {
    left: 14px;
    top: -8px;
    font-size: 168px;
    text-shadow: 2px 3px 2px var(--ink-shadow), -1px -1px 0 rgba(255,255,255,0.4);
    color: #e9e9e9;
  }
  .title--gedichte {
    left: 150px;
    top: 318px;
    font-size: 200px;
    transform: rotate(180deg);
    text-shadow: 0 0 10px var(--ink-shadow), 2px 2px 3px var(--ink-shadow);
    letter-spacing: 4px;
  }
  .title--helle {
    left: 680px;
    top: 608px;
    font-size: 200px;
    transform: rotate(180deg);
    text-shadow: 0 0 12px rgba(0,0,0,0.6), 2px 2px 3px rgba(0,0,0,0.5);
  }
</style>
</head>
<body>
  <main class="cover">
    <div class="side side--dark" role="img" aria-label="Dunkle Seite: kahler Baum als Silhouette vor alter Handschrift auf orangefarbenem Grund, oben und unten in Schwarz übergehend"></div>
    <div class="side side--light" role="img" aria-label="Helle Seite: Baumkrone und alte Handschrift auf braunem Band, oben und unten in Weiß übergehend"></div>
    <h1 class="title title--dunkle">dunkle</h1>
    <p class="title title--gedichte">Gedichte</p>
    <p class="title title--helle">helle</p>
  </main>
</body>
</html>
```